HiItsJonBrell.com needs a modern, eye-catching business card design

My name is Jon Brell and I own a video training (software development industry) website. I need a business card design that is eye catching for when I travel to conferences or do seminars. I would prefer something simple but bold. Something along the lines of this: https://pixvaultstatic.example/gallery_img/530172/44018/44018_9917302_530172_image.jpg

Note that I do not have a specific logo, but I do have an caricature I use on my site of myself. I've not attached it because I'm not really a fan of having it on my business cards. I would prefer lettering instead of an image. You can go to my website (https://hiitsjonbrell.com) for inspiration.

I want to add the following information on my card (the order of these, their size, and their casing is up to you):

Jon Brell
jon@HiItsJonBrell.com
@HiItsJonBrell
HiItsJonBrell.com
vidsharehub.example/HiItsJonBrell

I would also like to have somewhere on the card a small ad that says "Get a free course at https://HiItsJonBrell.com/FreeCourse". Feel free to play with that wording or layout if you need. I would prefer this text to be at the bottom of the card and subtle. Some small eye-catching thing might be ok but nothing huge or garish.

I plan on printing this card at pressquill.example (https://www.pressquill.example/us/design-guidelines/business-cards.html). I would like it to be the standard size (3.66" x 2.16"). I would prefer rounded corners and horizontal orientation. This is a two-side design. I would prefer the side with all of the information be primarily white but I like color text (again, flexible on that). On the front side, I like simple. Maybe just HiItsJonBrell.com (casing on that is up to you - whatever looks and reads the best - that goes for all of the casing). As for font choices, I prefer a modern, clean font. For example, Open Sans Light can be a nice option.

Website Info (might be helpful for the card):
Color Palette

Darkest blue - #263246
Alternate blue - #2F4E6A
Light blue - #2A98C3
Orange - #FF6201
White - #FFFFFF

Font for Jon Brell Logo

Jellyka Estryas Handwriting
http://www.typecrate.example/jellyka_estryas_handwriting.font

Fonts for Site Content and VidShare Thumbnails

Lovelo (bold title font)
http://www.glyphmill.example/lovelo-font/

Open Sans (body font)
http://www.letterbarn.example/fonts/open-sans

Industry/Entity Type

Software Development

Contact Information for Business Card

Jon Brell
jon@HiItsJonBrell.com
@HiItsJonBrell
HiItsJonBrell.com
vidsharehub.example/HiItsJonBrell

Get a free course at https://HiItsJonBrell.com/FreeCourse

Colors

Designer to choose colors to be used in the design.

Requirements
Nice to have
• Modern color - maybe primarily a color on the front and then that color as an accent on the back.
Should not have
• Lots of colors - I LOVE color but do not want a rainbow of colors on the card.

```html
<!DOCTYPE html>
<html lang="en">
<head>
<meta charset="utf-8">
<title>Jon Brell – Business Card</title>
<link rel="stylesheet" href="https://fonts.googleapis.com/css2?family=Josefin+Sans:wght@700&family=Open+Sans:wght@400;600;700&display=swap">
<style>
  :root {
    --page: #e6e6e6;
    --ink: #111111;
    --navy: #263246;
    --navy-alt: #2f4e6a;
    --sky: #2a98c3;
    --orange: #ff6201;
    --white: #ffffff;
    --paper: #f4f4f4;
    --charcoal: #38383d;
    --charcoal-deep: #1f1f23;
    --title-font: "Josefin Sans", sans-serif;
    --body-font: "Open Sans", sans-serif;
  }
  * { box-sizing: border-box; margin: 0; padding: 0; }
  html, body { width: 1200px; height: 960px; overflow: hidden; }
  body {
    position: relative;
    background: var(--page);
    font-family: var(--body-font);
    color: var(--navy);
  }
  .side-label {
    position: absolute;
    font-family: var(--title-font);
    font-weight: 700;
    font-size: 28px;
    letter-spacing: 14px;
    color: var(--ink);
    transform: translateX(-50%);
  }
  .side-label--front { left: 612px; top: 18px; }
  .side-label--back { left: 606px; top: 822px; }

  .divider {
    position: absolute;
    left: 124px; top: 438px;
    width: 951px; height: 6px;
    background: var(--ink);
    box-shadow: 0 3px 6px rgba(0,0,0,.25);
  }

  /* Front card */
  .front-card {
    position: absolute;
    left: 294px; top: 62px;
    width: 588px; height: 352px;
    background: var(--white);
    overflow: hidden;
    box-shadow: 10px 10px 16px rgba(0,0,0,.35);
  }
  .front-card__banner {
    position: absolute; left: 0; top: 0;
    width: 100%; height: 176px;
    background: linear-gradient(135deg, var(--charcoal) 0%, var(--charcoal-deep) 100%);
  }
  .front-card__portrait {
    position: absolute; left: 142px; top: 30px;
    width: 82px; height: 116px;
    border-radius: 40px 40px 20px 20px;
    background: linear-gradient(180deg, #4a4440 0%, #2f4a52 100%);
  }
  .front-card__wordmark {
    position: absolute; left: 232px; top: 74px;
    font-family: var(--body-font);
    font-weight: 400;
    font-size: 36px;
    letter-spacing: 6px;
    color: rgba(255,255,255,.55);
  }
  .front-card__stripe {
    position: absolute; left: 0; width: 100%;
    background: var(--orange);
  }
  .front-card__stripe--top { top: 176px; height: 5px; }
  .front-card__stripe--bottom { bottom: 0; height: 5px; }
  .front-card__tab {
    position: absolute; left: 134px; width: 320px;
  }
  .front-card__tab svg { display: block; }
  .front-card__tab span {
    position: absolute; left: 0; width: 100%;
    text-align: center;
    color: var(--white);
    font-size: 12.5px;
    line-height: 15px;
  }
  .front-card__tab--address { top: 176px; height: 38px; }
  .front-card__tab--address span { top: 11px; }
  .front-card__tab--offer { top: 306px; height: 46px; }
  .front-card__tab--offer span { top: 7px; font-size: 11.5px; line-height: 15px; }

  .front-card__identity {
    position: absolute; left: 94px; top: 242px;
    width: 150px; text-align: right;
  }
  .front-card__name {
    font-family: var(--title-font);
    font-weight: 700;
    font-size: 21px;
    letter-spacing: 5px;
    color: var(--navy);
    white-space: nowrap;
  }
  .front-card__role {
    display: inline-block;
    margin-top: 2px;
    font-size: 12px;
    color: var(--orange);
    text-decoration: underline;
    text-underline-offset: 2px;
  }
  .front-card__rule {
    position: absolute; left: 294px; top: 234px;
    width: 2px; height: 64px;
    background: var(--navy);
  }
  .contact-list {
    position: absolute; left: 346px; top: 233px;
    list-style: none;
  }
  .contact-list li {
    display: flex; align-items: center;
    height: 23px;
    font-size: 12px;
    color: var(--navy);
    white-space: nowrap;
  }
  .contact-list svg { width: 18px; height: 18px; margin-right: 9px; flex: none; }

  /* Back cards */
  .back-card {
    position: absolute;
    width: 366px; height: 220px;
    overflow: hidden;
    box-shadow: 9px 9px 14px rgba(0,0,0,.35);
    text-align: center;
  }
  .back-card--navy { left: 419px; top: 471px; background: var(--navy); color: var(--white); }
  .back-card--paper { left: 57px; top: 703px; background: var(--paper); color: var(--navy); }
  .back-card--sky { left: 782px; top: 704px; background: var(--sky); color: var(--white); }

  .back-card__offer {
    position: absolute; left: 0; top: 6px; width: 100%;
    font-size: 7px; line-height: 10px;
  }
  .back-card__offer strong { font-weight: 700; }
  .back-card__line {
    position: absolute; left: 0; width: 100%; height: 2px;
    background: var(--orange);
  }
  .back-card__line--top { top: 68px; }
  .back-card__line--bottom { top: 150px; }
  .back-card__portrait {
    position: absolute; left: 106px; top: 78px;
    width: 44px; height: 62px;
    border-radius: 22px 22px 12px 12px;
    background: linear-gradient(180deg, #c99a78 0%, #2f5a66 100%);
  }
  .back-card__wordmark {
    position: absolute; left: 158px; top: 92px;
    font-size: 20px; font-weight: 400;
    letter-spacing: 3px;
  }
  .back-card__role {
    position: absolute; left: 168px; top: 122px;
    font-size: 7.5px;
  }
  .back-card__site {
    position: absolute; left: 0; bottom: 10px; width: 100%;
    font-size: 7px; letter-spacing: 1px;
  }
</style>
</head>
<body>
  <div class="side-label side-label--front">FRONT</div>

  <section class="front-card">
    <div class="front-card__banner" role="img" aria-label="Dark backdrop of a code screen and keyboard"></div>
    <div class="front-card__portrait" role="img" aria-label="Illustrated portrait of Jon Brell"></div>
    <div class="front-card__wordmark">Jon Brell</div>
    <div class="front-card__stripe front-card__stripe--top"></div>

    <div class="front-card__tab front-card__tab--address">
      <svg width="320" height="38" viewBox="0 0 320 38"><polygon points="0,0 320,0 290,38 30,38" fill="var(--navy)"/></svg>
      <span>Your Company Address 9912-B</span>
    </div>

    <div class="front-card__identity">
      <div class="front-card__name">JON BRELL</div>
      <div class="front-card__role">Software Development</div>
    </div>
    <div class="front-card__rule"></div>

    <ul class="contact-list">
      <li>
        <svg viewBox="0 0 18 18"><circle cx="9" cy="9" r="8" fill="none" stroke="var(--orange)" stroke-width="2"/><circle cx="9" cy="9" r="3.5" fill="var(--orange)"/></svg>
        vidsharehub.example/HiItsJonBrell
      </li>
      <li>
        <svg viewBox="0 0 18 18"><circle cx="9" cy="9" r="9" fill="var(--orange)"/><rect x="4.5" y="6" width="9" height="6.5" fill="none" stroke="var(--white)" stroke-width="1"/><polyline points="4.5,6 9,10 13.5,6" fill="none" stroke="var(--white)" stroke-width="1"/></svg>
        jon@hiitsjonbrell.com
      </li>
      <li>
        <svg viewBox="0 0 18 18"><circle cx="9" cy="9" r="9" fill="var(--orange)"/><rect x="4.5" y="5" width="9" height="6.5" fill="none" stroke="var(--white)" stroke-width="1.2"/><line x1="7" y1="13.5" x2="11" y2="13.5" stroke="var(--white)" stroke-width="1.2"/></svg>
        https://hiitsjonbrell.com
      </li>
    </ul>

    <div class="front-card__tab front-card__tab--offer">
      <svg width="320" height="46" viewBox="0 0 320 46"><polygon points="30,0 290,0 320,46 0,46" fill="var(--navy)"/></svg>
      <span>Get a free course at<br>https://HiItsJonBrell.com/FreeCourse</span>
    </div>
    <div class="front-card__stripe front-card__stripe--bottom"></div>
  </section>

  <div class="divider"></div>

  <section class="back-card back-card--navy">
    <p class="back-card__offer"><strong>Get a free course at</strong><br>www.hiitsjonbrell.com/FreeCourse</p>
    <div class="back-card__line back-card__line--top"></div>
    <div class="back-card__portrait" role="img" aria-label="Illustrated portrait of Jon Brell"></div>
    <div class="back-card__wordmark">Jon Brell</div>
    <div class="back-card__role">Software Development</div>
    <div class="back-card__line back-card__line--bottom"></div>
    <p class="back-card__site">www.hiitsjonbrell.com</p>
  </section>

  <section class="back-card back-card--paper">
    <p class="back-card__offer"><strong>Get a free course at</strong><br>www.hiitsjonbrell.com/FreeCourse</p>
    <div class="back-card__line back-card__line--top"></div>
    <div class="back-card__portrait" role="img" aria-label="Illustrated portrait of Jon Brell"></div>
    <div class="back-card__wordmark">Jon Brell</div>
    <div class="back-card__role">Software Development</div>
    <div class="back-card__line back-card__line--bottom"></div>
    <p class="back-card__site">www.hiitsjonbrell.com</p>
  </section>

  <div class="side-label side-label--back">BACK</div>

  <section class="back-card back-card--sky">
    <p class="back-card__offer"><strong>Get a free course at</strong><br>www.hiitsjonbrell.com/FreeCourse</p>
    <div class="back-card__line back-card__line--top"></div>
    <div class="back-card__portrait" role="img" aria-label="Illustrated portrait of Jon Brell"></div>
    <div class="back-card__wordmark">Jon Brell</div>
    <div class="back-card__role">Software Development</div>
    <div class="back-card__line back-card__line--bottom"></div>
    <p class="back-card__site">www.hiitsjonbrell.com</p>
  </section>
</body>
</html>
```